Business Card Design

General Brief:
Verant Works is a newly established international manufacturing company. We have a manufacturing facility in China and are in the process of building a new facility in Brazil and are expanding into Africa, the Middle East and Western markets by marketing our products through a licensee program. We use production line manufacture processes (similar to the automotive industry) to produce houses, apartments, hotels and accommodation for the resource sector. We will need to be able to differentiate between the various regions that we serve and the market we operate in.

Key Words to describe our business:
International, Global, Professional, Quality, Standard Compliant, Designful, Cost Effective, Experienced

General Brief:
We need business card designs which cater for the possibility of differentiating the various regions that we serve and the market we operate in. Also, we need a secondary typography selection which suits the primary typography used in the corporate signature (please always state which font is being applied so as to cross-check for the necessary font licenses). First print will be made for our Chinese head office and division, therefore will have the special prerequisite of featuring two distinct languages: English-speaking and Chinese. We assume that a double sided version (recto/verso) could work best in order to separate the languages—other creative interpretations, options and integrations are welcome.

Logo Symbolism:
A dot might seem to be an unassuming little thing, the first mark on the pristine sheet of paper. In this case, the dot is a beginning. But see what just happened there? The dot, an essential component in the structure of the sentence, closed it, making it a symbol of ending. Therefore, the dot is both an origination and a conclusion, encompassing all the possibilities of the universe within it, a seed full of potential and a symbol of the supreme being. The dot is also called the "bindhu," which means "drop." The bindhu is a symbol of the absolute, marked on the forehead at the position of the third eye in the place believed to be the seat of the soul. The presence of dots outside or within a symbol can signify the presence of something else. It also acts as reminder of the concept of space and all in all performs as a very positive symbol in the Verant Works logo.
Updates

Target Market(s)

See Stationary Project

Industry/Entity Type

Accommodation

Requirements
Must have
• See Stationary Project

Logo on Stationary Project

Files

```html
<!DOCTYPE html>
<html lang="en">
<head>
<meta charset="utf-8">
<title>Verant Works — Business Card</title>
<link href="https://fonts.googleapis.com/css2?family=Open+Sans:wght@600;700&display=swap" rel="stylesheet">
<style>
  :root {
    --page-bg: #f2f2f4;
    --card-bg: #ffffff;
    --brand-blue: #00aeef;
    --brand-navy: #0d2c45;
    --body-text: #3f4347;
  }
  * { margin: 0; padding: 0; box-sizing: border-box; }
  html, body { width: 1200px; height: 900px; overflow: hidden; }
  body {
    background: var(--page-bg);
    font-family: "Open Sans", Arial, sans-serif;
    position: relative;
  }
  .card {
    position: absolute;
    top: 120px;
    width: 376px;
    height: 657px;
    background: var(--card-bg);
    overflow: hidden;
    box-shadow: 0 1px 6px rgba(0,0,0,0.25);
  }
  .card--front { left: 202px; border-top-right-radius: 46px; }
  .card--back  { left: 652px; border-top-left-radius: 46px; }

  .dot {
    position: absolute;
    border-radius: 50%;
    background: var(--brand-blue);
  }
  .dot--large  { left: 277px; top: 22px;  width: 76px; height: 76px; }
  .dot--medium { left: 228px; top: 102px; width: 30px; height: 30px; }
  .dot--small  { left: 303px; top: 166px; width: 12px; height: 12px; }
  .dot--edge   { left: 323px; top: 467px; width: 104px; height: 104px; }

  .company-name {
    position: absolute;
    display: flex;
    align-items: center;
    white-space: nowrap;
    color: var(--brand-navy);
    font-weight: 700;
    line-height: 1;
  }
  .company-name__dot {
    border-radius: 50%;
    background: var(--brand-blue);
    flex: none;
  }
  .company-name--front { left: 54px; top: 604px; font-size: 34px; transform: translateY(-100%); }
  .company-name--front .company-name__dot { width: 10px; height: 10px; margin-left: 8px; }

  .company-name--back { left: 0; right: 0; top: 64px; justify-content: center; font-size: 18px; }
  .company-name--back .company-name__dot { width: 6px; height: 6px; margin-left: 5px; }

  .contact {
    position: absolute;
    left: 0; right: 0; top: 191px;
    text-align: center;
    font-size: 13.5px;
    font-weight: 600;
    line-height: 21.5px;
    color: var(--body-text);
    font-style: normal;
  }

  .dot-row { position: absolute; top: 376px; left: 283px; display: flex; gap: 12px; }
  .dot-row span { width: 14px; height: 14px; border-radius: 50%; background: var(--brand-blue); }

  .band {
    position: absolute;
    left: 0; top: 468px;
    width: 303px; height: 102px;
    background: var(--brand-blue);
    border-radius: 0 51px 51px 0;
  }
</style>
</head>
<body>
  <section class="card card--front" aria-label="Card front">
    <span class="dot dot--large"></span>
    <span class="dot dot--medium"></span>
    <span class="dot dot--small"></span>
    <div class="company-name company-name--front">
      <span>Verant Works</span><span class="company-name__dot"></span>
    </div>
    <span class="dot dot--edge"></span>
  </section>

  <section class="card card--back" aria-label="Card back">
    <div class="company-name company-name--back">
      <span>Verant Works</span><span class="company-name__dot"></span>
    </div>
    <address class="contact">
      INTERNATIONAL MANUFACTURER<br>
      OF MODULAR HOMES<br>
      LOREM@VERANTWORKS.COM<br>
      18 HARBOR ROAD<br>
      LINHE TOWN<br>
      QINGSHAN DISTRICT NORTH CITY. CHINA<br>
      MOBILE: 0400123456
    </address>
    <div class="dot-row"><span></span><span></span><span></span></div>
    <div class="band"></div>
  </section>
</body>
</html>
```